Book Cover: When Lanterns Drift Over Quiet Harbor Towns
Subtitle: A handbook for noticing small signals so that every season feels calmer and kinder.
Author: Marcus Leland Dobrovin

I'd like to design the cover with the title on the top, the subtitle towards the middle or at least under the title, and a picture under the subtitle of a red heart that is beginning to crack at the top (and is slightly separated where cracked), but under the heart is a couple that is holding hands and using their other hands to hold up/together the heart so that it no longer cracks or breaks (it's as if they're pushing it back together/ensuring that it does not crack more).

Note: when drawing out the couple I'd like to avoid them having a specific skin color. Almost as if we can draw them without coloring them in. I do know that I'd like their hair to be dark. I hope that this makes sense, please feel free to call to me to discuss and use your judgement as well. My cell phone number is 1-555-613-2874.

This book is meant to educate and motivate others, and I truly believe that it can. With the right cover to catch people's eyes and pull them in we can be a success together. Thank you for your time and help!

Target Market(s)

Women, Couples, Single Individuals, Men (Women will probably be the main customer, but I hope that men buy it too as it can help everyone).

Industry/Entity Type

Motivation

Font styles to use
Serif
Decorative

Colors

Designer to choose colors to be used in the design.

Requirements
Must have
• I have described my idea within the project description.
• I am open to the artist using their ideas and colors too to make this cover stand out and to catch peoples eyes so that it is not dull. The book is meant to be motivational and educational so I think that brighter colors will catch people's eyes and also send positive vibes (vs darker - sending less positive vibes).
Nice to have
• Please see above and call me if you are confused, I am more than happy to discuss before you start your work (or during your work) 1-555-613-2874 my name is Marc.
• The book fonts I choose were typical for a book, and also creative. If you can somehow be creative, but not too wild I think that would do well. I hope that this makes sense, and again use your judgement, if normal/typical fonts look good go for it, but again if you believe you can add something unique and creative that is still elegant please try it out.
Should not have
• Please see book cover picture that I attached - This one seems too serious and I do not like the image as this heart is broken and this book is about avoiding heartbreak and finding the right person to be your true love and teammate in life. The image should be positive and warm if possible, and the people will hopefully be holding hands and holding up/together the heart that has BEGUN to crack and slightly separate down the middle.

```html
<!DOCTYPE html>
<html lang="en">
<head>
<meta charset="utf-8">
<title>When Lanterns Drift Over Quiet Harbor Towns — Book Cover</title>
<link rel="stylesheet" href="https://fonts.googleapis.com/css2?family=Raleway:wght@300;800&family=Grand+Hotel&family=Lato:wght@700&display=swap">
<style>
  :root {
    --cover-wine: #7c1326;
    --ink-white: #ffffff;
    --script-rose: #e9475c;
    --lace-white: #f6eeea;
    --lace-soft: #d9b9be;
    --bird-gold: #cdb36e;
    --bird-gold-deep: #a58c4c;
  }
  html, body {
    margin: 0;
    padding: 0;
    overflow: hidden;
    background: var(--cover-wine);
  }
  .cover {
    position: relative;
    width: 800px;
    height: 1200px;
    background: var(--cover-wine);
    color: var(--ink-white);
    overflow: hidden;
    text-align: center;
  }
  .title {
    position: absolute;
    top: 40px;
    left: 0;
    width: 800px;
    margin: 0;
    font-weight: normal;
  }
  .title-line {
    display: block;
    line-height: 1;
  }
  .title-light {
    font-family: "Raleway", sans-serif;
    font-weight: 300;
    font-size: 50px;
    letter-spacing: 1px;
  }
  .title-bold {
    font-family: "Raleway", sans-serif;
    font-weight: 800;
    font-size: 76px;
    margin: 2px 0 2px;
  }
  .title-large {
    font-size: 58px;
  }
  .title-script {
    font-family: "Grand Hotel", cursive;
    color: var(--script-rose);
    font-size: 138px;
    margin-top: -4px;
    line-height: 1.02;
  }
  .subtitle {
    position: absolute;
    top: 398px;
    left: 30px;
    width: 740px;
    margin: 0;
    font-family: "Lato", sans-serif;
    font-weight: 700;
    font-size: 31px;
    line-height: 1.16;
  }
  .art {
    position: absolute;
    display: block;
  }
  .art-heart   { left: 132px; top: 628px; width: 408px; height: 376px; }
  .art-bird-top   { left: 224px; top: 540px; width: 112px; height: 100px; }
  .art-bird-right { left: 604px; top: 752px; width: 148px; height: 100px; }
  .art-flourish   { left: 504px; top: 1004px; width: 244px; height: 60px; }
  .author {
    position: absolute;
    top: 1128px;
    left: 0;
    width: 800px;
    margin: 0;
    font-family: "Raleway", sans-serif;
    font-weight: 300;
    font-size: 34px;
    letter-spacing: 1px;
    text-transform: uppercase;
  }
</style>
</head>
<body>
  <main class="cover">
    <h1 class="title">
      <span class="title-line title-light">WHEN LANTERNS</span>
      <span class="title-line title-bold">DRIFT OVER</span>
      <span class="title-line title-light title-large">QUIET HARBOR</span>
      <span class="title-line title-script">Towns</span>
    </h1>
    <p class="subtitle">A handbook for noticing small signals so that every season feels calmer and kinder.</p>

    <svg class="art art-bird-top" viewBox="0 0 112 100" role="img" aria-label="Small golden bird perched on top of the heart">
      <defs>
        <linearGradient id="gold-a" x1="0" y1="0" x2="1" y2="1">
          <stop offset="0%" stop-color="var(--bird-gold)"/>
          <stop offset="100%" stop-color="var(--bird-gold-deep)"/>
        </linearGradient>
      </defs>
      <rect width="112" height="100" rx="40" fill="url(#gold-a)"/>
    </svg>

    <svg class="art art-heart" viewBox="0 0 408 376" role="img" aria-label="White lace-patterned ornamental heart">
      <defs>
        <radialGradient id="lace-fill" cx="50%" cy="45%" r="65%">
          <stop offset="0%" stop-color="var(--lace-white)"/>
          <stop offset="100%" stop-color="var(--lace-soft)"/>
        </radialGradient>
      </defs>
      <rect width="408" height="376" rx="36" fill="url(#lace-fill)"/>
    </svg>

    <svg class="art art-bird-right" viewBox="0 0 148 100" role="img" aria-label="Small golden bird carrying a white leaf">
      <defs>
        <linearGradient id="gold-b" x1="0" y1="0" x2="1" y2="1">
          <stop offset="0%" stop-color="var(--bird-gold)"/>
          <stop offset="100%" stop-color="var(--bird-gold-deep)"/>
        </linearGradient>
      </defs>
      <rect width="148" height="100" rx="40" fill="url(#gold-b)"/>
    </svg>

    <svg class="art art-flourish" viewBox="0 0 244 60" role="img" aria-label="Small white lace flourish trailing into dots">
      <rect width="244" height="60" rx="24" fill="var(--lace-soft)"/>
    </svg>

    <p class="author">Marcus Leland Dobrovin</p>
  </main>
</body>
</html>
```